BANNER FOR ONLINE CABINET COMPANY MAIN PAGE

Need 3 different banners for the main page. We are online platform for ordering cabinets, parts etc. online.
Website: trimfit.ca
A place where the banner will be placed: https://view.snapvault.example/qR7TpWzKmB4eX
Banner size: 1344x399 pixels
****Clients should get the main point that they can order everything online through the website.

Industry/Entity Type

online cabinets and parts ordering

Requirements
Must have
• online ordering icons, iphone, laptop, desktop pc - so clients get an idea that this is web based service to order cabinets

```html
<!DOCTYPE html>
<html lang="en">
<head>
<meta charset="utf-8">
<title>TrimFit – Veneer Doors &amp; Fronts</title>
<link rel="stylesheet" href="https://fonts.googleapis.com/css2?family=Montserrat:wght@300;400;500;700&family=Roboto:wght@300;400;500;700&display=swap">
<style>
  :root {
    --nav-bg: #3a3f44;
    --nav-text: #ffffff;
    --band-bg: #e4e5e6;
    --ink: #111111;
    --muted: #555a5e;
    --hero-dark: #2a2220;
    --accent-green: #2dba4e;
    --accent-orange: #f5a300;
    --dot-idle: #d4d4d4;
    --step-blue: #d9e9f7;
    --chat-bg: #3a3f44;
    --scroll: #f1f1f1;
  }
  * { box-sizing: border-box; margin: 0; padding: 0; }
  html, body { width: 1200px; height: 545px; overflow: hidden; background: #fff; }
  body { position: relative; font-family: "Roboto", Arial, sans-serif; color: var(--ink); }

  .site-nav { position: absolute; left: 0; top: 0; width: 1189px; height: 31px; background: var(--nav-bg); color: var(--nav-text); }
  .brand { position: absolute; left: 26px; top: 7px; font: 700 13px/17px "Roboto", sans-serif; color: var(--nav-text); display: flex; align-items: center; gap: 4px; }
  .brand-mark { width: 6px; height: 6px; background: #e0362a; margin-top: -8px; }
  .brand-divider { position: absolute; left: 99px; top: 6px; width: 1px; height: 19px; background: #fff; }
  .tagline { position: absolute; left: 111px; top: 10px; font-size: 8px; }
  .contact-box { position: absolute; left: 206px; top: 8px; width: 197px; height: 15px; background: #000; display: flex; align-items: center; font-size: 6.5px; padding-left: 6px; gap: 5px; }
  .contact-box svg { width: 8px; height: 8px; fill: none; stroke: #fff; stroke-width: 2; }
  .contact-box .phone-icon { fill: #fff; stroke: none; }
  .contact-box .hours { margin-left: 6px; }
  .nav-links { position: absolute; top: 0; height: 31px; left: 0; width: 100%; font-size: 7.5px; font-weight: 500; }
  .nav-links span { position: absolute; top: 11px; }
  .order-pill { position: absolute; left: 719px; top: 8px; width: 62px; height: 15px; border-radius: 8px; background: var(--accent-green); font-size: 7.5px; font-weight: 500; text-align: center; line-height: 15px; }
  .nav-icon { position: absolute; top: 9px; width: 12px; height: 12px; fill: none; stroke: #fff; stroke-width: 1.6; }

  .intro-band { position: absolute; left: 0; top: 31px; width: 1189px; height: 58px; background: var(--band-bg); text-align: center; }
  .intro-band h1 { font: 700 19.5px/1 "Roboto", sans-serif; letter-spacing: 0.6px; margin-top: 7px; }
  .intro-band p { font: 300 13.5px/1 "Roboto", sans-serif; color: var(--muted); margin-top: 8px; }

  .hero { position: absolute; left: 0; top: 89px; width: 1189px; height: 355px; overflow: hidden; box-shadow: 0 2px 4px rgba(0,0,0,.25); }
  .hero-photo { position: absolute; inset: 0; background: linear-gradient(180deg, #f4f4f2 0%, #ececea 55%, #e2e1de 66%, #c99a6c 80%, #b98857 100%); }
  .hero-art { position: absolute; inset: 0; }
  .hero-copy { position: absolute; left: 74px; top: 0; color: #fff; font-family: "Montserrat", sans-serif; }
  .hero-title { position: absolute; top: 70px; left: 0; white-space: nowrap; font-weight: 700; font-size: 47px; line-height: 1; letter-spacing: 0.3px; }
  .hero-subtitle { position: absolute; top: 124px; left: 0; white-space: nowrap; font-weight: 400; font-size: 48px; line-height: 1; color: transparent; -webkit-text-stroke: 1px #d8d8d8; }
  .hero-rule { position: absolute; top: 188px; left: 0; width: 400px; height: 1.5px; background: #fff; }
  .hero-points { position: absolute; top: 212px; left: 0; white-space: nowrap; font-size: 12.6px; line-height: 19px; }
  .hero-cta { position: absolute; top: 270px; left: 0; width: 188px; height: 35px; border: 1px solid #fff; font-weight: 700; font-size: 12.5px; line-height: 33px; text-align: center; }

  .online-devices { position: absolute; top: 266px; left: 210px; width: 150px; }
  .device-row { display: flex; align-items: flex-end; gap: 12px; height: 28px; }
  .device-row svg { fill: none; stroke: #fff; stroke-width: 1.5; stroke-linejoin: round; }
  .device-caption { margin-top: 5px; font-size: 8.5px; font-weight: 500; letter-spacing: 0.3px; white-space: nowrap; color: #e6e6e6; }

  .slider-dots { position: absolute; top: 448px; left: 544px; display: flex; gap: 8px; }
  .slider-dots i { width: 7.5px; height: 7.5px; background: var(--dot-idle); display: block; }
  .slider-dots i.active { background: var(--accent-orange); }

  .steps-heading { position: absolute; top: 477px; left: 0; width: 1189px; text-align: center; font: 700 20px/1 "Roboto", sans-serif; letter-spacing: 0.5px; }
  .step-num { position: absolute; top: 527px; font: 700 60px/1 "Montserrat", sans-serif; color: var(--step-blue); }
  .step-icon { position: absolute; top: 541px; width: 14px; height: 8px; border: 1.5px solid #3c8fd6; border-bottom: none; border-radius: 2px 2px 0 0; }

  .chat-tab { position: absolute; left: 1025px; top: 525px; width: 149px; height: 20px; background: var(--chat-bg); color: #fff; font-size: 7px; font-weight: 500; line-height: 20px; padding-left: 8px; border-radius: 4px 4px 0 0; }
  .chat-tab::after { content: ""; position: absolute; right: -4px; top: -3px; width: 12px; height: 12px; border-radius: 50%; background: var(--accent-green); }
  .scroll-rail { position: absolute; right: 0; top: 0; width: 11px; height: 545px; background: var(--scroll); }
  .scroll-thumb { position: absolute; right: 2px; top: 6px; width: 7px; height: 82px; background: #c1c1c1; }
</style>
</head>
<body>
  <header class="site-nav">
    <div class="brand">TrimFit<span class="brand-mark"></span></div>
    <div class="brand-divider"></div>
    <div class="tagline">Get the size you need!</div>
    <div class="contact-box">
      <svg class="phone-icon" viewBox="0 0 24 24"><path d="M6.6 10.8a15 15 0 0 0 6.6 6.6l2.2-2.2c.3-.3.7-.4 1-.2 1.1.4 2.3.6 3.6.6.6 0 1 .4 1 1V20c0 .6-.4 1-1 1A17 17 0 0 1 3 4c0-.6.4-1 1-1h3.5c.6 0 1 .4 1 1 0 1.3.2 2.5.6 3.6.1.3 0 .7-.2 1z"/></svg>
      <span>Call us (403) 555 0182</span>
      <svg class="hours" viewBox="0 0 24 24"><circle cx="12" cy="12" r="9"/><path d="M12 7v5l3 2"/></svg>
      <span>Mon-Fri 8AM - 4.30PM</span>
    </div>
    <nav class="nav-links">
      <span style="left:691px">CAD</span>
      <span class="order-pill">ORDER NOW</span>
      <span style="left:794px">DESIGN &amp; QUOTE</span>
      <span style="left:867px">SAMPLES</span>
      <span style="left:914px">ABOUT</span>
      <span style="left:953px">CONTACT</span>
      <span style="left:1001px">ARTICLES</span>
    </nav>
    <svg class="nav-icon" style="left:1057px" viewBox="0 0 24 24"><circle cx="10" cy="10" r="6"/><path d="M15 15l6 6"/></svg>
    <svg class="nav-icon" style="left:1094px;stroke-width:3" viewBox="0 0 24 24"><path d="M8 8a4 4 0 1 1 6 3.4c-1.3.8-2 1.6-2 3.1V16"/><circle cx="12" cy="21" r="0.8"/></svg>
    <svg class="nav-icon" style="left:1130px" viewBox="0 0 24 24"><circle cx="12" cy="8" r="4.5"/><path d="M3 22c1-5 5-7 9-7s8 2 9 7z"/></svg>
    <svg class="nav-icon" style="left:1164px" viewBox="0 0 24 24"><path d="M2 4h3l3 11h11l2-8H7"/><circle cx="9" cy="19" r="1.5"/><circle cx="17" cy="19" r="1.5"/></svg>
  </header>

  <section class="intro-band">
    <h1>THE FIRST ONLINE CUSTOM CABINET’S MANUFACTURER</h1>
    <p>Order custom cabinets online with instant price calculator. No hidden fees, top quality warranty.</p>
  </section>

  <section class="hero">
    <div class="hero-photo" role="img" aria-label="Bright white kitchen with brick wall, white cabinets, range hood, wooden counter and white chairs"></div>
    <svg class="hero-art" width="1189" height="355" viewBox="0 0 1189 355">
      <polygon points="454,0 478,0 680,355 650,355" fill="#8a8785" opacity="0.55"/>
      <polygon points="0,0 454,0 650,355 0,355" fill="var(--hero-dark)"/>
    </svg>
    <div class="hero-copy">
      <div class="hero-title">VENEER DOORS</div>
      <div class="hero-subtitle">&amp; FRONTS</div>
      <div class="hero-rule"></div>
      <div class="hero-points">Lots of colors in stock-Everythilng made besed on your size<br>Very durable Material - Easyto clean</div>
      <div class="hero-cta">CHECK OPTIONS</div>
      <div class="online-devices" aria-label="Order on phone, laptop or desktop">
        <div class="device-row">
          <svg width="14" height="24" viewBox="0 0 14 24"><rect x="1" y="1" width="12" height="22" rx="2"/><path d="M5.5 19.5h3"/></svg>
          <svg width="38" height="22" viewBox="0 0 38 22"><rect x="6" y="1" width="26" height="16" rx="1.5"/><path d="M1 20.5h36"/></svg>
          <svg width="32" height="28" viewBox="0 0 32 28"><rect x="1" y="1" width="30" height="19" rx="1.5"/><path d="M13 20v5M19 20v5M9 26.5h14"/></svg>
        </div>
        <div class="device-caption">Order everything online</div>
      </div>
    </div>
  </section>

  <div class="slider-dots"><i></i><i></i><i></i><i></i><i class="active"></i><i></i><i></i></div>

  <h2 class="steps-heading">EASY QUOTE &amp; ORDER</h2>
  <div class="step-num" style="left:262px">1</div><div class="step-icon" style="left:309px"></div>
  <div class="step-num" style="left:426px">2</div><div class="step-icon" style="left:480px;width:8px"></div>
  <div class="step-num" style="left:597px">3</div><div class="step-icon" style="left:646px;width:6px"></div>
  <div class="step-num" style="left:780px">4</div><div class="step-icon" style="left:818px"></div>

  <div class="chat-tab">Questions? Start chat, we are online!</div>
  <div class="scroll-rail"><div class="scroll-thumb"></div></div>
</body>
</html>
```